Business card based on your logo design "Marlowe&Co"

Can you please design a business card based on the logo artwork you designed for our business. Double sided as per your submitted image of possible application of logo.

```html
<!DOCTYPE html>
<html lang="en">
<head>
<meta charset="utf-8">
<title>Marlowe&amp;Co Business Card</title>
<link rel="stylesheet" href="https://fonts.googleapis.com/css2?family=Oswald:wght@500;600&family=Open+Sans:wght@400;600&display=swap">
<style>
  :root {
    --bg: #3a3234;
    --card-white: #ffffff;
    --band-grey: #efefef;
    --rule-grey: #d9d9d9;
    --ink: #2b2b2b;
    --ink-soft: #444444;
    --orange: #f7941d;
    --orange-light: #f9a83a;
    --charcoal: #3d3d3d;
    --charcoal-deep: #2a2a2a;
    --white: #ffffff;
  }
  * { margin: 0; padding: 0; box-sizing: border-box; }
  html, body { width: 1200px; height: 1000px; overflow: hidden; }
  body {
    background: var(--bg);
    font-family: "Open Sans", Arial, sans-serif;
    position: relative;
  }
  .card {
    position: absolute;
    left: 230px;
    width: 740px;
    height: 423px;
    overflow: hidden;
    box-shadow: 0 10px 30px rgba(0,0,0,0.35);
  }
  .card-front { top: 50px; background: var(--card-white); }
  .card-back {
    top: 527px;
    background: radial-gradient(ellipse at 35% 40%, var(--charcoal) 0%, var(--charcoal-deep) 100%);
  }

  /* Front */
  .edge-band { position: absolute; left: 0; right: 0; height: 30px; background: var(--band-grey); }
  .edge-band.top { top: 0; }
  .edge-band.bottom { bottom: 0; }
  .front-wordmark {
    position: absolute; left: 46px; top: 56px;
    font-family: "Oswald", Arial, sans-serif; font-weight: 600;
    font-size: 40px; letter-spacing: 1px; color: var(--ink);
    line-height: 1;
  }
  .rule-grey { position: absolute; left: 0; top: 112px; width: 470px; height: 5px; background: var(--rule-grey); }
  .contact-list { position: absolute; left: 46px; top: 170px; list-style: none; }
  .contact-list li {
    display: flex; align-items: center; gap: 10px;
    font-size: 15px; font-weight: 600; color: var(--ink-soft);
    height: 23px;
  }
  .contact-list svg { width: 14px; height: 14px; fill: var(--orange); flex: none; }
  .contact-list .no-icon { padding-left: 24px; }
  .company-block { position: absolute; right: 40px; top: 150px; text-align: right; }
  .address { font-size: 15px; font-weight: 600; color: var(--ink-soft); }
  .company-name {
    margin-top: 10px;
    font-family: "Oswald", Arial, sans-serif; font-weight: 500;
    font-size: 24px; color: var(--orange); letter-spacing: 0.5px;
  }
  .rule-orange { position: absolute; right: 0; top: 232px; width: 300px; height: 5px; background: var(--orange); }
  .person { position: absolute; right: 40px; top: 282px; text-align: right; }
  .person-name {
    font-family: "Oswald", Arial, sans-serif; font-weight: 500;
    font-size: 28px; color: var(--ink); letter-spacing: 0.5px; line-height: 1.1;
  }
  .person-name .first { color: var(--orange); }
  .person-role { font-size: 15px; font-weight: 600; color: var(--ink-soft); margin-top: 2px; }

  /* Back */
  .back-wordmark {
    position: absolute; left: 0; right: 0; top: 150px; text-align: center;
    font-family: "Oswald", Arial, sans-serif; font-weight: 600;
    font-size: 72px; letter-spacing: 2px; color: var(--white); line-height: 1;
  }
  .accent-band {
    position: absolute; left: 0; right: 24px; bottom: 34px; height: 20px;
    background: linear-gradient(90deg, var(--orange-light), var(--orange));
  }
  .accent-corner {
    position: absolute; right: 24px; bottom: 34px; width: 20px; height: 70px;
    background: var(--orange);
  }
</style>
</head>
<body>

<section class="card card-front" aria-label="Business card front">
  <div class="edge-band top"></div>
  <div class="edge-band bottom"></div>
  <div class="front-wordmark">MARLOWE&amp;CO</div>
  <div class="rule-grey"></div>

  <ul class="contact-list">
    <li>
      <svg viewBox="0 0 24 24" aria-hidden="true"><path d="M6.6 10.8a15.1 15.1 0 0 0 6.6 6.6l2.2-2.2a1 1 0 0 1 1-.25 11.4 11.4 0 0 0 3.6.57 1 1 0 0 1 1 1V20a1 1 0 0 1-1 1A17 17 0 0 1 3 4a1 1 0 0 1 1-1h3.5a1 1 0 0 1 1 1c0 1.25.2 2.45.57 3.57a1 1 0 0 1-.25 1z"/></svg>
      000 - 4821 - 3907
    </li>
    <li>
      <svg viewBox="0 0 24 24" aria-hidden="true"><path d="M7 1h10a2 2 0 0 1 2 2v18a2 2 0 0 1-2 2H7a2 2 0 0 1-2-2V3a2 2 0 0 1 2-2zm0 3v14h10V4zm5 15.5a1 1 0 1 0 0 2 1 1 0 0 0 0-2z"/></svg>
      000 - 6150 - 2784
    </li>
    <li>
      <svg viewBox="0 0 24 24" aria-hidden="true"><path d="M2 5h20v14H2zm2 2v.5l8 5 8-5V7zm0 2.9V17h16V9.9l-8 5z"/></svg>
      hello@marloweandco.com
    </li>
    <li>
      <svg viewBox="0 0 24 24" aria-hidden="true"><path d="M10.6 13.4a1 1 0 0 1 0-1.4l3.5-3.5a3 3 0 0 1 4.2 4.2l-2.1 2.1-1.4-1.4 2.1-2.1a1 1 0 0 0-1.4-1.4L12 13.4a1 1 0 0 1-1.4 0zM9.1 8.3l1.4 1.4-2.1 2.1a1 1 0 0 0 1.4 1.4l.7-.7 1.4 1.4-.7.7a3 3 0 0 1-4.2-4.2z"/></svg>
      marloweandco.com
    </li>
  </ul>

  <div class="company-block">
    <div class="address">418 Harbor Lane, Portland 97201</div>
    <div class="company-name">MARLOWE &amp; CO</div>
  </div>
  <div class="rule-orange"></div>

  <div class="person">
    <div class="person-name"><span class="first">ODETTE</span> MARLOWE</div>
    <div class="person-role">Manager / CEO</div>
  </div>
</section>

<section class="card card-back" aria-label="Business card back">
  <div class="back-wordmark">MARLOWE&amp;CO</div>
  <div class="accent-band"></div>
  <div class="accent-corner"></div>
</section>

</body>
</html>
```